BrivoPeak Business Card Design Project

We are looking for a modern, clean business card design for our new company. We are a consulting firm focused on the financial services market providing management and IT consulting to banks, insurance companies, etc. Please include our company logo and company contact information from the attached file in the design. Two versions of the logo are attached, either version is acceptable. Logos are available in other file formats if needed. We would like to include the contact information for both our UK and US offices as well as the following information for each individual card holder: Name, position/title, address, phone number and e-mail address.
Updates
Project Deadline Extended
Reason: A last minute trip over seas has prevented us from finalizing the decision. A decision will be made this week. We apologize for the inconvenience.
Industry/Entity Type
Business
Contact Information for Business Card
Company logo.
Company locations and phone numbers for both the US and UK offices.
Company URL.
Cardholder Name
Cardholder Position/title
Cardholder Address
Cardholder Phone Number
Cardholder e-mail Address
Look and feel
Each slider illustrates characteristics of the customer's brand and the style your logo design should communicate.

```html
<!DOCTYPE html>
<html lang="en">
<head>
<meta charset="utf-8">
<title>BrivoPeak Business Card</title>
<link href="https://fonts.googleapis.com/css2?family=PT+Sans:wght@400;700&display=swap" rel="stylesheet">
<style>
  :root {
    --navy-deep: #13284f;
    --navy: #1d3a6b;
    --paper: #ffffff;
    --ink-grey: #5a5d63;
    --rule: #ffffff;
    --backdrop: #ecebe7;
  }
  * { box-sizing: border-box; margin: 0; padding: 0; }
  html, body {
    width: 1200px; height: 843px; overflow: hidden;
    background: var(--backdrop);
    font-family: "PT Sans", sans-serif;
  }
  .stage {
    width: 1200px; height: 843px;
    display: flex; justify-content: center; align-items: center; gap: 110px;
  }
  .card {
    width: 340px; height: 595px; position: relative;
    box-shadow: 0 10px 28px rgba(0,0,0,0.18);
  }
  .card::before {
    content: ""; position: absolute; inset: 14px;
    border: 2px solid var(--frame-colour);
    pointer-events: none;
  }
  .card--front { background: var(--paper); --frame-colour: var(--navy-deep); }
  .card--back {
    background: linear-gradient(160deg, var(--navy) 0%, var(--navy-deep) 100%);
    --frame-colour: var(--rule);
    color: var(--paper);
    display: flex; flex-direction: column; align-items: center;
    padding: 58px 40px 0;
    text-align: center;
  }
  .front-brand {
    position: absolute; top: 50%; left: 50%; transform: translate(-50%, -50%);
    display: flex; align-items: center; gap: 12px;
    font-size: 34px; font-weight: 700; color: var(--ink-grey); letter-spacing: 0.5px;
  }
  .brand-square { width: 18px; height: 18px; background: var(--navy-deep); }
  .back-brand {
    font-size: 22px; font-weight: 700; letter-spacing: 0.5px;
    display: flex; align-items: center; gap: 8px;
  }
  .back-brand .brand-square { width: 12px; height: 12px; background: var(--paper); }
  .holder-name { font-size: 24px; margin-top: 18px; }
  .holder-title { font-size: 15px; margin-top: 2px; }
  .divider {
    width: 210px; margin: 26px 0 12px;
    display: flex; align-items: center; gap: 10px;
  }
  .divider::before, .divider::after {
    content: ""; flex: 1; height: 1px; background: var(--rule); opacity: 0.85;
  }
  .icon { width: 14px; height: 14px; fill: var(--paper); display: block; }
  .icon--inline { margin: 8px auto 6px; }
  .detail { font-size: 15px; line-height: 1.35; }
</style>
</head>
<body>
<svg width="0" height="0" style="position:absolute">
  <defs>
    <symbol id="i-pin" viewBox="0 0 24 24"><path d="M12 2a7 7 0 0 0-7 7c0 5 7 13 7 13s7-8 7-13a7 7 0 0 0-7-7zm0 9.5A2.5 2.5 0 1 1 12 6.5a2.5 2.5 0 0 1 0 5z"/></symbol>
    <symbol id="i-phone" viewBox="0 0 24 24"><path d="M6.6 10.8a15 15 0 0 0 6.6 6.6l2.2-2.2a1 1 0 0 1 1-.25 11.4 11.4 0 0 0 3.6.57 1 1 0 0 1 1 1V20a1 1 0 0 1-1 1A17 17 0 0 1 3 4a1 1 0 0 1 1-1h3.5a1 1 0 0 1 1 1c0 1.25.2 2.45.57 3.6a1 1 0 0 1-.25 1z"/></symbol>
    <symbol id="i-mail" viewBox="0 0 24 24"><path d="M3 5h18a1 1 0 0 1 1 1v12a1 1 0 0 1-1 1H3a1 1 0 0 1-1-1V6a1 1 0 0 1 1-1zm9 7.5L4 7.2V8l8 5.3L20 8v-.8z"/></symbol>
    <symbol id="i-globe" viewBox="0 0 24 24"><path d="M12 2a10 10 0 1 0 0 20 10 10 0 0 0 0-20zm6.9 6h-2.9a15 15 0 0 0-1.4-3.6A8 8 0 0 1 18.9 8zM12 4a13 13 0 0 1 1.9 4h-3.8A13 13 0 0 1 12 4zM4.3 14a8 8 0 0 1 0-4h3.4a16 16 0 0 0 0 4zm.8 2h2.9a15 15 0 0 0 1.4 3.6A8 8 0 0 1 5.1 16zM8 8H5.1a8 8 0 0 1 4.3-3.6A15 15 0 0 0 8 8zm4 12a13 13 0 0 1-1.9-4h3.8A13 13 0 0 1 12 20zm2.3-6H9.7a14 14 0 0 1 0-4h4.6a14 14 0 0 1 0 4zm.3 5.6A15 15 0 0 0 16 16h2.9a8 8 0 0 1-4.3 3.6zM16.3 14a16 16 0 0 0 0-4h3.4a8 8 0 0 1 0 4z"/></symbol>
  </defs>
</svg>

<main class="stage">
  <section class="card card--front">
    <div class="front-brand"><span class="brand-square"></span>BrivoPeak</div>
  </section>

  <section class="card card--back">
    <div class="back-brand"><span class="brand-square"></span>BrivoPeak</div>
    <h1 class="holder-name">Daniel Ashford</h1>
    <p class="holder-title">CEO/Founder</p>

    <div class="divider"><svg class="icon"><use href="#i-pin"/></svg></div>
    <p class="detail">4120 Linden Court<br>Juneau, Alaska 34581</p>
    <svg class="icon icon--inline"><use href="#i-phone"/></svg>
    <p class="detail">689 555 0142</p>

    <div class="divider"><svg class="icon"><use href="#i-pin"/></svg></div>
    <p class="detail">4120 Linden Court<br>Juneau, Alaska 34581</p>
    <svg class="icon icon--inline"><use href="#i-phone"/></svg>
    <p class="detail">689 555 0142</p>

    <div class="divider"><svg class="icon"><use href="#i-mail"/></svg></div>
    <p class="detail">name@brivopeak.com</p>
    <svg class="icon icon--inline"><use href="#i-globe"/></svg>
    <p class="detail">www.brivopeak.com</p>
  </section>
</main>
</body>
</html>
```